P&H RESTORATION

I want a brochure similiar to the example i've attached.
My company name is P&H Restoration. The website is: P-H-Restoration.com.
The phone number is 803.417.9056.

I don't like the "yellow" being the main color of the example so I'm open to suggestions. I want something CLEAN & Simple, like our logo . This will be a bi fold brochure

```html
<!DOCTYPE html>
<html lang="en">
<head>
<meta charset="utf-8">
<title>P&amp;H Restoration – Bi-fold Brochure Cover</title>
<link rel="stylesheet" href="https://fonts.googleapis.com/css2?family=Montserrat:wght@500;600;700;800&family=Roboto:wght@400&display=swap">
<style>
  :root {
    --canvas: #efe3d4;
    --paper: #ffffff;
    --paper-grey: #ececec;
    --ink: #111111;
    --orange: #e87722;
    --orange-deep: #d9661a;
    --photo-dark: #3a1d0c;
    --photo-mid: #7a3d14;
    --photo-warm: #c2621d;
  }
  * { box-sizing: border-box; margin: 0; padding: 0; }
  html, body { width: 1200px; height: 800px; overflow: hidden; }
  body {
    background: var(--canvas);
    position: relative;
    font-family: "Montserrat", Arial, sans-serif;
    color: var(--ink);
  }
  .spread {
    position: absolute;
    left: 120px;
    top: 30px;
    width: 960px;
    height: 740px;
    display: flex;
  }
  .panel {
    position: relative;
    width: 480px;
    height: 740px;
    overflow: hidden;
  }
  .panel--back { background: linear-gradient(160deg, #fafafa 0%, #f1f1f1 100%); }
  .panel--front { background: linear-gradient(200deg, #f4f4f4 0%, var(--paper-grey) 100%); }
  .panel-art {
    position: absolute;
    inset: 0;
    width: 100%;
    height: 100%;
  }
  .brand {
    position: absolute;
    display: flex;
    align-items: center;
    gap: 10px;
    font-family: "Montserrat", Arial, sans-serif;
    font-weight: 600;
    font-size: 19px;
    color: var(--ink);
    letter-spacing: 0.02em;
    white-space: nowrap;
  }
  .brand-mark {
    width: 16px;
    height: 16px;
    border: 2px solid var(--ink);
  }
  .panel--back .brand { left: 56px; top: 372px; }
  .panel--front .brand { right: 56px; top: 78px; }

  .back-headline {
    position: absolute;
    left: 56px;
    top: 428px;
    font-weight: 800;
    font-size: 22px;
    line-height: 1.35;
    white-space: nowrap;
  }
  .accent-bar {
    position: absolute;
    height: 5px;
    width: 62px;
  }
  .accent-bar--orange { background: var(--orange); left: 56px; top: 512px; }
  .accent-bar--black { background: var(--ink); left: 50px; top: 652px; width: 60px; }
  .back-contact {
    position: absolute;
    left: 56px;
    top: 540px;
    font-family: "Roboto", Arial, sans-serif;
    font-size: 17px;
    line-height: 1.75;
  }

  .front-title {
    position: absolute;
    left: 50px;
    top: 520px;
    white-space: nowrap;
  }
  .front-title-lead {
    display: block;
    font-weight: 700;
    font-size: 24px;
    letter-spacing: 0.01em;
  }
  .front-title-main {
    display: block;
    font-weight: 700;
    font-size: 54px;
    line-height: 1;
    color: var(--orange-deep);
    margin-top: 2px;
  }
  .front-url {
    position: absolute;
    left: 50px;
    top: 672px;
    font-family: "Montserrat", Arial, sans-serif;
    font-weight: 500;
    font-size: 21px;
  }
</style>
</head>
<body>
  <main class="spread">
    <section class="panel panel--back">
      <svg class="panel-art" viewBox="0 0 480 740">
        <defs>
          <linearGradient id="blueprint-tone" x1="0" y1="0" x2="1" y2="1">
            <stop offset="0" stop-color="#e8862c"/>
            <stop offset="0.5" stop-color="#b9621c"/>
            <stop offset="1" stop-color="#e07a22"/>
          </linearGradient>
        </defs>
        <polygon points="150,0 350,0 480,300 480,640 200,230" fill="url(#blueprint-tone)" role="img" aria-label="Rolled architectural blueprints in an orange tint"/>
        <polygon points="110,180 220,180 200,320" fill="var(--orange)"/>
      </svg>
      <div class="brand"><span class="brand-mark"></span>P&amp;H Restoration</div>
      <h2 class="back-headline">Insurance Claim?<br>We're on Your Team.</h2>
      <div class="accent-bar accent-bar--orange"></div>
      <p class="back-contact">803.417.9056.<br>P-H-Restoration.com.</p>
    </section>

    <section class="panel panel--front">
      <svg class="panel-art" viewBox="0 0 480 740">
        <defs>
          <linearGradient id="interior-tone" x1="0" y1="0" x2="1" y2="1">
            <stop offset="0" stop-color="var(--photo-dark)"/>
            <stop offset="0.45" stop-color="var(--photo-mid)"/>
            <stop offset="0.75" stop-color="var(--photo-warm)"/>
            <stop offset="1" stop-color="#6b6660"/>
          </linearGradient>
        </defs>
        <polygon points="40,200 400,200 480,250 480,740 440,740 300,460 0,460 0,260" fill="url(#interior-tone)" role="img" aria-label="Interior of a house under restoration with exposed beams and support posts"/>
        <polygon points="405,590 480,590 480,710 365,710" fill="var(--orange)" opacity="0.88"/>
      </svg>
      <div class="brand"><span class="brand-mark"></span>P&amp;H Restoration</div>
      <h1 class="front-title">
        <span class="front-title-lead">Insurance Claim</span>
        <span class="front-title-main">Specialist</span>
      </h1>
      <div class="accent-bar accent-bar--black"></div>
      <p class="front-url">p-h-restoration.com</p>
    </section>
  </main>
</body>
</html>
```